Tri fold flyer design for restoration company

Use our website for inspiration and make a world class advertising tri fold flyer.
brookvalerestoration.com

Colors
0054AA
0677BA
7BADD7
CADEEF
E8F1F8
00AB8E
00BBA5
67D7C9
C6EFE9
E9F9F6
EB3D1F
EC4F4E
F09395
F8D3D4
FCEDEE

```html
<!DOCTYPE html>
<html lang="en">
<head>
<meta charset="utf-8">
<title>Brookvale Restoration – Tri Fold Flyer</title>
<link rel="stylesheet" href="https://fonts.googleapis.com/css2?family=Jost:wght@400;500;600&family=Source+Sans+3:wght@400;600;700&family=Nunito:wght@900&display=swap">
<style>
  :root{
    --navy:#1c4a8a;
    --orange:#d9441f;
    --sky:#a4d5f1;
    --sky-head:#8cc4ea;
    --ink:#1d1d1f;
    --white:#ffffff;
  }
  *{margin:0;padding:0;box-sizing:border-box}
  html,body{width:939px;height:1200px;overflow:hidden;background:var(--white)}
  body{position:relative;font-family:"Source Sans 3",Arial,sans-serif;color:var(--ink)}
  .panel{position:absolute;left:145px;width:652px;height:462px;background:var(--white);box-shadow:3px 3px 5px rgba(0,0,0,.35);overflow:hidden}
  .panel--outside{top:109px}
  .panel--inside{top:623px}
  .shapes{position:absolute;inset:0}
  .abs{position:absolute}

  /* outside panel */
  .intro{left:20px;top:17px;width:183px;color:var(--white);font-weight:700;font-size:8px;line-height:10.3px}
  .intro p{margin-bottom:4px}
  .benefits{left:14px;top:115px;width:192px;list-style:none;color:var(--white);font-weight:700;font-size:8px;line-height:10.2px}
  .benefits li{position:relative;padding-left:17px;margin-bottom:4.6px}
  .benefits svg{position:absolute;left:0;top:1px;width:12px;height:12px}
  .follow{left:252px;top:26px;font-family:"Jost",sans-serif;color:var(--white);font-size:13.5px;letter-spacing:.3px}
  .social{left:252px;top:47px;display:flex;gap:7px}
  .social span{width:15px;height:15px;border-radius:50%;background:var(--orange);display:block}
  .brand{left:452px;top:218px;display:flex;align-items:center;gap:6px}
  .brand-square{width:14px;height:14px;background:var(--orange)}
  .brand-name{font-family:"Jost",sans-serif;font-weight:600;font-size:18px;color:var(--navy);letter-spacing:.2px}
  .tagline{left:441px;top:304px;font-family:"Jost",sans-serif;font-weight:500;font-size:16px;color:var(--ink)}
  .call{left:302px;top:403px;display:flex;align-items:center;gap:8px;color:var(--white);font-family:"Jost",sans-serif;font-weight:500;font-size:17.5px}
  .call svg{width:18px;height:18px}
  .phone{left:248px;top:428px;font-family:"Jost",sans-serif;font-weight:600;font-size:24.5px;color:var(--white);letter-spacing:.3px}
  .features{left:450px;top:343px;list-style:none;color:var(--white);font-family:"Jost",sans-serif;font-weight:500;font-size:11.6px;line-height:14.5px}
  .features li{position:relative;padding-left:42px;margin-bottom:4.5px}
  .features svg{position:absolute;left:0;top:-2px;width:24px;height:20px}

  /* inside panel */
  .about{left:20px;top:20px;width:632px;font-size:9px;line-height:11.2px}
  .about p{margin-bottom:4.4px}
  .about-wrap{float:right;width:160px;height:170px;margin-top:-20px;shape-outside:polygon(2px 0,160px 0,160px 175px,2px 175px,54px 83px,54px 88px)}
  .service{position:absolute;top:189px;height:273px;padding:20px 18px 0 20px}
  .service--dark{background:var(--navy);color:var(--white)}
  .service--light{background:var(--sky);color:var(--ink)}
  .service h2{display:flex;align-items:center;gap:6px;font-family:"Nunito",sans-serif;font-weight:900;font-size:10.4px;line-height:12px;height:34px;margin-bottom:6px;letter-spacing:.2px}
  .service--dark h2{color:var(--sky-head)}
  .service--light h2{color:var(--orange)}
  .service h2 svg{flex:none}
  .service p{font-size:7.9px;line-height:10.2px;margin-bottom:10px}
  .photo{position:absolute}
</style>
</head>
<body>

<section class="panel panel--outside">
  <svg class="shapes" viewBox="0 0 652 462" width="652" height="462">
    <defs>
      <linearGradient id="gWater" x1="0" y1="0" x2="1" y2="1"><stop offset="0" stop-color="#2f86cf"/><stop offset=".5" stop-color="#8fd0f2"/><stop offset="1" stop-color="#3c97d8"/></linearGradient>
      <linearGradient id="gFire" x1="0" y1="0" x2="1" y2="1"><stop offset="0" stop-color="#3a1a0c"/><stop offset=".45" stop-color="#e5521c"/><stop offset="1" stop-color="#f3a23a"/></linearGradient>
      <linearGradient id="gHouse" x1="0" y1="0" x2="0" y2="1"><stop offset="0" stop-color="#66803e"/><stop offset=".55" stop-color="#8a8c7e"/><stop offset="1" stop-color="#5c7a3a"/></linearGradient>
      <linearGradient id="gWall" x1="0" y1="0" x2="1" y2="1"><stop offset="0" stop-color="#8f8a80"/><stop offset="1" stop-color="#d4d0c8"/></linearGradient>
    </defs>
    <polygon points="0,0 414,0 0,445" fill="var(--navy)"/>
    <polygon role="img" aria-label="Photo of weathered concrete wall" points="0,462 206,238 206,462" fill="url(#gWall)"/>
    <polygon role="img" aria-label="Photo of splashing clear water" points="414,0 652,0 547,135 321,135" fill="url(#gWater)"/>
    <polygon role="img" aria-label="Photo of flames" points="652,15 539,135 652,251" fill="url(#gFire)"/>
    <polygon role="img" aria-label="Photo of a storm-damaged house with a fallen tree" points="218,228 294,148 511,148 341,336 218,462" fill="url(#gHouse)"/>
    <polygon points="341,336 434,336 434,462 218,462" fill="var(--orange)"/>
    <rect x="434" y="336" width="218" height="126" fill="var(--navy)"/>
  </svg>

  <div class="abs intro">
    <p>At Brookvale Restoration NY, we don't believe in doing things by half measures.</p>
    <p>Our restoration professionals are passionate about helping you re-establish your home or business and get your life back to normal quickly.</p>
    <p>We take pride in delivering exceptional results and making properties look like new again!</p>
  </div>

  <ul class="abs benefits">
    <li><svg viewBox="0 0 12 12"><circle cx="6" cy="6" r="6" fill="var(--orange)"/><path d="M3.3 6.2l1.9 1.8 3.5-3.6" stroke="#fff" stroke-width="1.4" fill="none"/></svg>We believe in Long Term Relationship and provide professional and quick services.</li>
    <li><svg viewBox="0 0 12 12"><circle cx="6" cy="6" r="6" fill="var(--orange)"/><path d="M3.3 6.2l1.9 1.8 3.5-3.6" stroke="#fff" stroke-width="1.4" fill="none"/></svg>We have many years of experience in handling disasters in a professional way.</li>
    <li><svg viewBox="0 0 12 12"><circle cx="6" cy="6" r="6" fill="var(--orange)"/><path d="M3.3 6.2l1.9 1.8 3.5-3.6" stroke="#fff" stroke-width="1.4" fill="none"/></svg>We are highly Trained, equipped with Modern Equipment and Machines, and dedicated to reshape things fast</li>
    <li><svg viewBox="0 0 12 12"><circle cx="6" cy="6" r="6" fill="var(--orange)"/><path d="M3.3 6.2l1.9 1.8 3.5-3.6" stroke="#fff" stroke-width="1.4" fill="none"/></svg>We are available 24/7 to handle any size<br>disaster.</li>
    <li><svg viewBox="0 0 12 12"><circle cx="6" cy="6" r="6" fill="var(--orange)"/><path d="M3.3 6.2l1.9 1.8 3.5-3.6" stroke="#fff" stroke-width="1.4" fill="none"/></svg>We have specialized disaster teams that<br>are expert in particular type of<br>disasters.</li>
    <li><svg viewBox="0 0 12 12"><circle cx="6" cy="6" r="6" fill="var(--orange)"/><path d="M3.3 6.2l1.9 1.8 3.5-3.6" stroke="#fff" stroke-width="1.4" fill="none"/></svg>We are Fast, Reliable, Dedicated,<br>Professional and Expert to<br>analyze and handle<br>situations perfectly.</li>
  </ul>

  <div class="abs follow">Follow Us On</div>
  <div class="abs social" aria-label="Social media links"><span></span><span></span><span></span></div>

  <div class="abs brand"><span class="brand-square"></span><span class="brand-name">Brookvale Restoration</span></div>
  <div class="abs tagline">Restoration Services in NY</div>

  <div class="abs call">
    <svg viewBox="0 0 18 18"><circle cx="9" cy="9" r="9" fill="#fff"/><path d="M6 4.8c.4-.3.9-.2 1.1.2l.8 1.5c.2.4.1.8-.2 1l-.6.5c.5 1.1 1.4 2 2.5 2.5l.5-.6c.3-.3.7-.4 1-.2l1.5.8c.4.2.5.7.2 1.1l-.6.8c-.4.5-1.1.7-1.700.4C8.4 11.800 6.200 9.600 5.200 7.200c-.3-.6-.1-1.300.4-1.700z" fill="var(--orange)"/></svg>
    Call Now!!!
  </div>
  <div class="abs phone">(555) 014-2290</div>

  <ul class="abs features">
    <li><svg viewBox="0 0 24 20"><ellipse cx="12" cy="10" rx="12" ry="10" fill="var(--orange)"/><path d="M7.5 11V9.5a4.5 4.5 0 0 1 9 0V11" stroke="#fff" stroke-width="1.2" fill="none"/><rect x="6.5" y="10" width="2" height="3.5" rx=".8" fill="#fff"/><rect x="15.5" y="10" width="2" height="3.5" rx=".8" fill="#fff"/></svg>24/7 Emergency Service</li>
    <li><svg viewBox="0 0 24 20"><ellipse cx="12" cy="10" rx="12" ry="10" fill="var(--orange)"/><circle cx="12.5" cy="10.5" r="5" stroke="#fff" stroke-width="1.2" fill="none"/><path d="M12.5 8v2.7l1.8 1.2M11.5 4.5h2" stroke="#fff" stroke-width="1.2" fill="none"/></svg>Rapid Response, Quality<br>Results</li>
    <li><svg viewBox="0 0 24 20"><ellipse cx="12" cy="10" rx="12" ry="10" fill="var(--orange)"/><circle cx="12" cy="8" r="2.6" stroke="#fff" stroke-width="1.2" fill="none"/><path d="M7 15.5c.5-2.6 2.6-4 5-4s4.5 1.4 5 4" stroke="#fff" stroke-width="1.2" fill="none"/></svg>Trained, Certified Service<br>Professionals</li>
    <li><svg viewBox="0 0 24 20"><ellipse cx="12" cy="10" rx="12" ry="10" fill="var(--orange)"/><circle cx="12" cy="10" r="5" stroke="#fff" stroke-width="1.1" fill="none"/><path d="M9.8 10.1l1.6 1.5 2.8-2.9" stroke="#fff" stroke-width="1.2" fill="none"/></svg>RCSA Certified Firm</li>
  </ul>
</section>

<section class="panel panel--inside">
  <svg class="photo" style="left:0;top:0" width="652" height="189" viewBox="0 0 652 189">
    <defs>
      <linearGradient id="gStorm" x1="0" y1="0" x2="0" y2="1"><stop offset="0" stop-color="#4d5258"/><stop offset=".55" stop-color="#8a7a6a"/><stop offset="1" stop-color="#a0512e"/></linearGradient>
      <linearGradient id="gMold" x1="0" y1="0" x2="1" y2="0"><stop offset="0" stop-color="#e6e8ea"/><stop offset=".6" stop-color="#c9cdd0"/><stop offset="1" stop-color="#8c8a84"/></linearGradient>
    </defs>
    <polygon role="img" aria-label="Photo of storm debris and a wrecked building under grey sky" points="498,0 652,0 652,83 548,83" fill="url(#gStorm)"/>
    <polygon role="img" aria-label="Photo of a technician in protective suit removing mold from a wall" points="548,93 652,93 652,177 498,177" fill="url(#gMold)"/>
  </svg>

  <div class="abs about">
    <div class="about-wrap" aria-hidden="true"></div>
    <p>Brookvale Restoration NY Offers Water Damage, Fire Damage, and Mold Remediation Services. Proudly Serving Suffolk, Nassau, and Surrounding Areas.</p>
    <p>Our Certified Technicians work with ALL insurance carriers</p>
    <p>If you have recently faced a disaster, you may feel devastated, like nothing will ever be the same. At Brookvale Restoration NY, we'll work tirelessly to return life to normal for you and your family or employees. Brookvale Restoration NY has gathered a team of experts in the field of property restoration.</p>
    <p>By combining professional service with our desire to exceed expectations, we ensure your property – no matter the previous damage – is returned to a like-new state. Using innovative practices, we'll go to work providing restoration services for your home or business.</p>
    <p>We work with commercial and residential property owners who have recently endured flash floods, fires, or mold infestations. Using the latest techniques and equipment, we provide reliable service that you can count on.</p>
  </div>

  <div class="service service--dark" style="left:0;width:162px">
    <h2><svg width="26" height="20" viewBox="0 0 26 20"><path d="M1 3c3-2 5 2 8 0s5-2 8 0 5 2 8 0M1 8c3-2 5 2 8 0s5-2 8 0 5 2 8 0M1 13c3-2 5 2 8 0s5-2 8 0 5 2 8 0M1 18c3-2 5 2 8 0s5-2 8 0 5 2 8 0" stroke="var(--sky-head)" stroke-width="1.3" fill="none"/></svg>WATER DAMAGE</h2>
    <p>Water damage is quite common among other disasters. A little amount of water in your home can create a huge loss and damage. This happens when we neglect this little amount and it becomes big within short span of time. The damage that can be repaired immediately takes few thousand dollars. This can damage antique furniture, wooden floors, expensive carpets, electric appliances, and lot more.</p>
    <p>Water also leads to form mold and becomes a great threat. Moisture in any part of area gives the ground for mold formation, bacteria and many insects. This needs immediate care by Our experts before it becomes huge.</p>
  </div>

  <div class="service service--light" style="left:162px;width:161px;padding-left:17px">
    <h2><svg width="22" height="30" viewBox="0 0 22 30"><path d="M11 1c1 6 10 9 10 18a10 10 0 0 1-20 0c0-5 4-7 4-11 3 2 3 5 3 7 3-3 4-8 3-14z" fill="var(--orange)"/><path d="M11 15c2 3 5 5 5 9a5 5 0 0 1-10 0c0-3 3-5 5-9z" fill="var(--sky)"/></svg>FIRE AND SMOKE<br>DAMAGE</h2>
    <p>Fire incidents are very common and can happen anytime. This experi- ence is very frustrating for home owners and they are not sure what to do in such a disaster. This has to be handled very carefully by experts as many materials, equipments etc can blast, emit toxic gases, make construction weak and many things they are unaware.</p>
    <p>At Brookvale, we have team of experts that is ready to handle and manage such situations and provide professional service to get back in shape.</p>
  </div>

  <div class="service service--dark" style="left:323px;width:164px;padding-left:16px">
    <h2><svg width="44" height="30" viewBox="0 0 44 30"><path d="M9 19a7 7 0 0 1 1-13 9 9 0 0 1 17 1 6 6 0 0 1 8 6 6 6 0 0 1-5 6" stroke="var(--sky-head)" stroke-width="1.6" fill="none"/><path d="M17 13l-4 8h4l-3 8 8-10h-4l3-6z" fill="var(--sky-head)"/><path d="M24 22h10c3 0 3-3 1-3M22 26h14" stroke="var(--sky-head)" stroke-width="1.5" fill="none"/></svg>WEATHER<br>DAMAGE</h2>
    <p>We are not sure of natural calamities that can happen anywhere, anytime. It can be anything like storm, lightning, earthquake that creates a huge loss and damage to properties. These are the situations that are very frustrating as we don't have the idea or experience to handle them. These needs to be handled by experts and professional teams so the things can be normal and back in shape as early as possible.</p>
    <p>We are professional and experts in handling these situations and help homeowners to get their property back in shape as efficiently as possible. Our professional teams treat all property damage with immense care.</p>
  </div>

  <div class="service service--light" style="left:487px;width:165px">
    <h2><svg width="40" height="34" viewBox="0 0 40 34"><ellipse cx="24" cy="12" rx="11" ry="7" transform="rotate(-35 24 12)" stroke="var(--orange)" stroke-width="1.6" fill="none"/><circle cx="22" cy="13" r="1.3" fill="var(--orange)"/><circle cx="27" cy="9" r="1.3" fill="var(--orange)"/><circle cx="24" cy="16" r="1.1" fill="var(--orange)"/><path d="M16 20c-4 3-6 6-12 12M19 22c-3 3-6 6-10 10" stroke="var(--orange)" stroke-width="1.4" fill="none"/></svg>MOLD</h2>
    <p>The development of Mold comes with moisture, excessive water, flooding, and many type of water leakages. This mold growth is huge threat to the belongings when it grows. It should be handled at first sight as it grows at fast rate and change the appearance of things. It should be stopped from growing or spreading any further.</p>
    <p>If the mold is left unchecked, it could further result in reduced indoor air quality and an unsafe environment. Molds can also attack paper, card- board, and organic adhesives, as well as wallpaper and particle board.</p>
  </div>
</section>

</body>
</html>
```